Modern luxury trendy cosmetics label

Looking for a cosmetics packaging label design. We are looking for a professionel, modern and luxury look like Lorena Vasquel, Meadowkin Apothecary, Marigold Tessin, Gavin Albert Pruke, Zuna, Orvik + Dalle, Velumi, Sleepy Walrus, the plainfold, lumiere de sable.Name of product: Nordic Tulip Mask - Needle-Free Contour Ritual Ingredients that have scientific proof of anti aging: Cherry blossom extact, collegen, hyaluronic acid, coconut oil. Color of product itself: Pastel pink. Smell: Cherry blossom. Colors of label: simple and black and white or some subtle colors.

Target Market(s)

Women, luxury market, modern women, young and old women

Industry/Entity Type

Cosmetics

Font styles to use
Sans Serif

Colors

Designer to choose colors to be used in the design.

Requirements
Must have
• A modern look, professional, cosmetics, beauty, professional market, original

```html
<!DOCTYPE html>
<html lang="en">
<head>
<meta charset="utf-8">
<title>Nordic Tulip Mask – Label</title>
<link rel="stylesheet" href="https://fonts.googleapis.com/css2?family=Open+Sans:ital,wght@0,300;0,400;0,700;1,700&display=swap">
<style>
  :root {
    --ink: #1a1a1a;
    --label-line: #3a3a3a;
    --paper: #ffffff;
    --canvas: #ffffff;
    --blossom: #e8788f;
  }
  * { margin: 0; padding: 0; box-sizing: border-box; }
  html, body {
    width: 1200px;
    height: 1021px;
    overflow: hidden;
    background: var(--canvas);
  }
  body {
    position: relative;
    font-family: "Open Sans", sans-serif;
    color: var(--ink);
  }
  .label {
    position: absolute;
    left: 203px;
    top: 65px;
    width: 794px;
    height: 890px;
    background: var(--paper);
    border: 3px solid var(--label-line);
  }
  .brand {
    position: absolute;
    left: 226px;
    top: 44px;
    font-weight: 300;
    font-size: 112px;
    line-height: 1;
    letter-spacing: 1px;
  }
  .brand-tagline {
    position: absolute;
    left: 230px;
    top: 190px;
    font-weight: 700;
    font-size: 23px;
    letter-spacing: -0.3px;
    text-transform: uppercase;
    white-space: nowrap;
  }
  .product-name {
    position: absolute;
    writing-mode: vertical-rl;
    transform: rotate(180deg);
    font-size: 66px;
    line-height: 1;
    text-transform: uppercase;
    white-space: nowrap;
  }
  .product-name--origin {
    left: 74px;
    bottom: 176px;
    font-weight: 300;
  }
  .product-name--title {
    left: 182px;
    bottom: 96px;
    font-weight: 300;
  }
  .product-name strong { font-weight: 700; }
  .claims {
    position: absolute;
    right: 86px;
    top: 432px;
    text-align: right;
    text-transform: uppercase;
  }
  .claim-primary {
    font-weight: 700;
    font-size: 40px;
    line-height: 1.2;
  }
  .claim-secondary {
    font-weight: 300;
    font-size: 40px;
    line-height: 1.25;
    display: inline-block;
    padding-bottom: 12px;
    border-bottom: 5px solid var(--blossom);
  }
  .claim-benefit {
    margin-top: 10px;
    font-weight: 700;
    font-size: 38px;
    line-height: 1.2;
  }
  .ingredients {
    margin-top: 36px;
    list-style: none;
    font-size: 23px;
    line-height: 1.8;
    font-weight: 400;
  }
  .ingredients-heading {
    font-weight: 700;
    font-size: 23px;
  }
  .ingredients-heading em {
    text-transform: none;
    font-style: italic;
  }
</style>
</head>
<body>
  <section class="label">
    <div class="brand">orvela</div>
    <div class="brand-tagline">The Radiance Atelier</div>

    <h1 class="product-name product-name--origin">Nordic</h1>
    <div class="product-name product-name--title">Tulip <strong>Mask</strong></div>

    <div class="claims">
      <div class="claim-primary">Needle-Free</div>
      <div class="claim-secondary">Contour Ritual</div>
      <div class="claim-benefit">Anti Aging</div>
      <ul class="ingredients">
        <li class="ingredients-heading"><em>Scientific Proof</em> INGREDIENTS</li>
        <li>Cherry Blossom Extract</li>
        <li>Collagen</li>
        <li>Hyaluronic Acid</li>
        <li>Coconut Oil</li>
      </ul>
    </div>
  </section>
</body>
</html>
```